Business Card / Appointment Card for Physician

On one side it should give the logo, address, and contact information, and on the other side it should br an Appointment card.

One Side:
Logo (see attached files)
Board Certified American Orthopedic Surgery

1487 Harrowgate Ave.
Suite KM7
Bronx, NY 10527
Tel: (718) 552 - 1948
Fax: (718) 552 - 7210

628 Fourth Ave.
Suite 42
New York, NY 10087
Tel: (212) 734 - 2815

Second Side:
Appointment
give them a choice of Bronx or Mahattan office
For:
Date:
Time:

If you are unable to keep your appointment, please call (718) 263-5102 24hrs in advance.

Target Market(s)

People that need orthopedic surgery

Industry/Entity Type

Business

Contact Information for Business Card

smart and attractive

Requirements
Must have
• logo
• contact information on one side, appointment information on the other

```html
<!DOCTYPE html>
<html lang="en">
<head>
<meta charset="utf-8">
<title>Daniel R. Ashford MD PC – Business &amp; Appointment Card</title>
<link rel="stylesheet" href="https://fonts.googleapis.com/css2?family=Questrial&display=swap">
<style>
  :root {
    --page-bg: #e7eaee;
    --card-white: #fbfbfb;
    --brand-blue: #1b8ccb;
    --brand-blue-deep: #1566a8;
    --brand-green: #7bbf45;
    --ink-blue: #1a68ad;
    --rule-grey: #b9bec4;
    --label-grey: #5f6670;
    --white: #ffffff;
  }
  * { box-sizing: border-box; margin: 0; padding: 0; }
  html, body {
    width: 1200px; height: 780px; overflow: hidden;
    background: var(--page-bg);
    font-family: "Questrial", "Century Gothic", sans-serif;
  }
  .card {
    position: absolute; top: 236px;
    width: 540px; height: 308px;
    background: var(--card-white);
    overflow: hidden;
    box-shadow: 0 6px 18px rgba(0,0,0,.14);
  }
  .card--front { left: 40px; }
  .card--back { left: 620px; }

  /* Brand block */
  .brand { display: flex; align-items: center; gap: 14px; }
  .brand__dot {
    width: 64px; height: 64px; border-radius: 50%;
    background: var(--brand-blue); flex: none;
  }
  .brand__name {
    color: var(--ink-blue); font-size: 25px; letter-spacing: .5px;
    text-transform: uppercase; line-height: 1;
  }
  .brand__specialty {
    color: var(--ink-blue); font-size: 10.5px; letter-spacing: .6px;
    text-transform: uppercase; margin-top: 5px;
  }

  /* Front */
  .front__brand-area {
    height: 168px; display: flex; align-items: center; justify-content: center;
  }
  .front__offices {
    height: 104px; background: var(--brand-blue);
    display: flex; align-items: center; justify-content: center;
    color: var(--white); font-size: 14px; line-height: 1.45;
  }
  .office { padding: 0 22px; }
  .office--manhattan { text-align: right; }
  .office__divider { width: 1px; height: 70px; background: rgba(255,255,255,.75); }
  .contact-line { display: flex; align-items: center; gap: 6px; }
  .office--manhattan .contact-line { justify-content: flex-end; }
  .contact-icon { width: 14px; height: 14px; flex: none; }
  .front__credential {
    height: 36px; background: var(--brand-green);
    border-top: 3px solid var(--white);
    color: var(--white); font-size: 15px; letter-spacing: .6px;
    display: flex; align-items: center; justify-content: center;
  }

  /* Back */
  .back__body { padding: 22px 34px 0; height: 250px; position: relative; }
  .back__body .brand { justify-content: flex-end; }
  .back__body .brand__name { font-size: 21px; text-align: right; }
  .back__body .brand__specialty { font-size: 9.5px; text-align: right; }
  .rule { height: 1px; background: var(--rule-grey); }
  .appointment__title {
    color: var(--ink-blue); font-size: 21px; padding: 10px 0 8px; text-align: center;
  }
  .weekdays { display: flex; justify-content: space-between; padding: 12px 6px 10px; }
  .weekday { display: flex; align-items: center; gap: 6px; color: var(--label-grey); font-size: 12px; }
  .weekday__box { width: 17px; height: 17px; border: 1px solid var(--label-grey); background: var(--white); }
  .schedule { display: flex; align-items: flex-end; gap: 10px; color: var(--label-grey); font-size: 13px; }
  .schedule__field { flex: 1; border-bottom: 1px solid var(--rule-grey); height: 18px; }
  .schedule__field--time { flex: .8; }
  .schedule__meridiem { line-height: 1.1; font-size: 12px; }
  .back__notice {
    position: absolute; left: 0; right: 0; bottom: 0; height: 58px;
    background: var(--brand-blue-deep);
    border-top: 5px solid var(--brand-green);
    color: var(--white); font-size: 12.5px; line-height: 1.45;
    display: flex; flex-direction: column; justify-content: center; padding-left: 34px;
  }
  .back__notice strong { font-weight: 400; letter-spacing: .4px; }
</style>
</head>
<body>

<section class="card card--front" aria-label="Business card front">
  <div class="front__brand-area">
    <div class="brand">
      <span class="brand__dot" aria-hidden="true"></span>
      <div>
        <div class="brand__name">Daniel R. Ashford MD PC</div>
        <div class="brand__specialty">Orthopaedic Surgery &amp; Sports Medicine</div>
      </div>
    </div>
  </div>

  <div class="front__offices">
    <div class="office office--manhattan">
      <div>628 Fourth Ave.</div>
      <div>Suite 42, New York, NY 10087</div>
      <div class="contact-line">(212) 734 - 2815
        <svg class="contact-icon" viewBox="0 0 14 14" aria-label="Telephone"><circle cx="7" cy="7" r="6.3" fill="none" stroke="#fff" stroke-width="1.2"/><path d="M4.5 4h1.6l.6 1.5-.9.7c.4.9 1 1.5 1.9 1.9l.7-.9 1.5.6V9.5c0 .4-.3.6-.7.6A5.2 5.2 0 0 1 3.9 4.7c0-.4.2-.7.6-.7z" fill="#fff"/></svg>
      </div>
    </div>
    <span class="office__divider" aria-hidden="true"></span>
    <div class="office office--bronx">
      <div>1487 Harrowgate Ave.</div>
      <div>Suite KM7, Bronx, NY 10527</div>
      <div class="contact-line">
        <svg class="contact-icon" viewBox="0 0 14 14" aria-label="Telephone"><circle cx="7" cy="7" r="6.3" fill="none" stroke="#fff" stroke-width="1.2"/><path d="M4.5 4h1.6l.6 1.5-.9.7c.4.9 1 1.5 1.9 1.9l.7-.9 1.5.6V9.5c0 .4-.3.6-.7.6A5.2 5.2 0 0 1 3.9 4.7c0-.4.2-.7.6-.7z" fill="#fff"/></svg>
        (718) 552 - 1948</div>
      <div class="contact-line">
        <svg class="contact-icon" viewBox="0 0 14 14" aria-label="Fax"><circle cx="7" cy="7" r="6.3" fill="none" stroke="#fff" stroke-width="1.2"/><rect x="4" y="6" width="6" height="4" fill="#fff"/><rect x="5" y="3.5" width="4" height="2.5" fill="none" stroke="#fff" stroke-width=".9"/></svg>
        (718) 552 - 7210</div>
    </div>
  </div>

  <div class="front__credential">Board Certified American Orthopedic Surgery</div>
</section>

<section class="card card--back" aria-label="Appointment card">
  <div class="back__body">
    <div class="brand">
      <div>
        <div class="brand__name">Daniel R. Ashford MD PC</div>
        <div class="brand__specialty">Orthopaedic Surgery &amp; Sports Medicine</div>
      </div>
    </div>
    <div class="rule" style="margin-top:12px"></div>
    <div class="appointment__title">Has An Appointment On</div>
    <div class="rule"></div>
    <div class="weekdays">
      <label class="weekday"><span class="weekday__box"></span>Mon</label>
      <label class="weekday"><span class="weekday__box"></span>Tues</label>
      <label class="weekday"><span class="weekday__box"></span>Wed</label>
      <label class="weekday"><span class="weekday__box"></span>Thur</label>
      <label class="weekday"><span class="weekday__box"></span>Fri</label>
      <label class="weekday"><span class="weekday__box"></span>Sat</label>
    </div>
    <div class="schedule">
      <span>Date</span><span class="schedule__field"></span>
      <span>AT</span><span class="schedule__field schedule__field--time"></span>
      <span class="schedule__meridiem">am.<br>pm.</span>
    </div>
  </div>
  <div class="back__notice">
    <span>If you are unable to keep your appointment, please call</span>
    <span><strong>(718) 263-5102</strong> 24hrs in advance.</span>
  </div>
</section>

</body>
</html>
```